New website for Pilates Studio

I need a new version of my website
http://brightcoreflow.biz/
I want an updated fresh look with an easier to read schedule that looks good on mobile phones as well as laptops.
Clean, simple, fresh and BOLD

Target Market(s)

All ages, genders and races

Coding

Number of Pages Required

Colors
9bcb3c

Requirements
Must have
• Photos that mostly use the real images from our studio. Browse our facebook page, website or ask me for high quality images

```html
<!DOCTYPE html>
<html lang="en">
<head>
<meta charset="utf-8">
<title>Bright Core Flow – Pilates &amp; Spiral Flow Studio</title>
<link href="https://fonts.googleapis.com/css2?family=Open+Sans:wght@400;600;700&family=Noto+Serif:ital@1&display=swap" rel="stylesheet">
<style>
:root{
  --green-light:#9bcb3c;
  --green-nav:#86ad46;
  --green-nav-dark:#6e9435;
  --green-active:#4d6a2b;
  --green-card:#4b5f2b;
  --green-accent:#7ea330;
  --olive:#6d7a1f;
  --text:#333;
  --muted:#777;
  --line:#e3e3e3;
  --grey-band:#f0f0f0;
  --footer:#2a2a2a;
  --white:#fff;
}
*{box-sizing:border-box;margin:0;padding:0}
html,body{width:824px;height:1200px;overflow:hidden}
body{position:relative;background:var(--white);font-family:"Open Sans",Arial,sans-serif;color:var(--text)}
.wrap{position:absolute;left:61px;width:702px}
.serif-sub{font-family:"Noto Serif",Georgia,serif;font-style:italic}

/* header */
.site-header{position:absolute;top:0;left:0;width:824px;height:66px}
.brand{position:absolute;left:61px;top:15px;display:flex;align-items:center;gap:7px}
.brand-dot{width:30px;height:30px;border-radius:50%;background:var(--olive)}
.brand-name{font-size:20px;font-weight:700;color:var(--olive);line-height:1}
.brand-tag{font-size:7.5px;color:var(--olive);font-weight:600;margin-top:3px;letter-spacing:.3px}
.call{position:absolute;left:601px;top:27px;font-size:10px;color:var(--olive)}
.badge{position:absolute;left:733px;top:18px;width:30px;height:30px;border-radius:50%;background:#2f7b7c}

/* nav */
.main-nav{position:absolute;top:66px;left:0;width:824px;height:38px;background:linear-gradient(var(--green-nav),var(--green-nav-dark))}
.main-nav ul{list-style:none;position:absolute;left:61px;top:0;display:flex;height:38px}
.main-nav li{font-size:10.5px;letter-spacing:1.3px;color:var(--white);line-height:38px;padding:0 17px}
.main-nav li.active{background:var(--green-active);clip-path:polygon(0 0,92% 0,100% 50%,92% 100%,0 100%);padding:0 24px 0 20px}
.social{position:absolute;left:667px;top:10px;display:flex;gap:5px}
.social span{width:19px;height:19px;background:var(--green-active);border:1px solid rgba(255,255,255,.5)}

/* hero */
.hero{position:absolute;top:104px;left:0;width:824px;height:395px;background:linear-gradient(120deg,#bfc4c0,#9c9a93 45%,#c8b7a8 75%,#a7a9a4)}
.hero-title{position:absolute;top:172px;width:824px;text-align:center;font-size:40px;color:var(--white);text-shadow:0 1px 3px rgba(0,0,0,.3)}
.hero-arrow{position:absolute;top:178px;font-size:30px;color:rgba(255,255,255,.35)}

/* info cards */
.card{position:absolute;top:427px;width:229px;height:145px;padding:10px 15px;box-shadow:0 1px 3px rgba(0,0,0,.2)}
.card h2{font-size:19px;font-weight:400;letter-spacing:.4px;line-height:1.2}
.card .serif-sub{font-size:9.5px;margin-bottom:6px}
.card-light{left:61px;background:var(--white)}
.card-light h2{color:var(--green-card)}
.card-dark{background:var(--green-card);color:var(--white)}
.card-dark .serif-sub{color:#dfe7cf}
.row{display:flex;justify-content:space-between;font-size:9px;height:31px;align-items:center;border-bottom:1px solid var(--line)}
.row:last-child{border-bottom:none}
.card-dark .row{border-color:rgba(255,255,255,.2)}
.clock{display:flex;align-items:center;gap:14px}
.pager{position:absolute;right:15px;top:14px;display:flex;gap:3px}
.pager span{width:15px;height:14px;border:1px solid #bbb;font-size:9px;line-height:12px;text-align:center}
.pt-body{display:flex;gap:14px;margin-top:6px}
.pt-body p{font-size:7.6px;line-height:12px}
.more{display:inline-block;margin-top:8px;background:var(--white);color:var(--text);font-size:7.5px;padding:2px 8px;width:54px}

/* about */
.section-title{position:absolute;left:0;width:824px;text-align:center;font-size:20px;font-weight:400}
.section-title em{font-style:normal;color:var(--green-accent)}
.about-text{position:absolute;top:639px;left:78px;width:668px;text-align:center;font-size:8.2px;line-height:14.4px;color:var(--muted)}

/* services */
.service{position:absolute;top:760px;width:229px;text-align:center}
.service .photo{height:114px;border:3px solid var(--white);box-shadow:0 1px 3px rgba(0,0,0,.25)}
.service h3{font-size:12.5px;font-weight:400;margin-top:11px}
.service p{font-size:7.8px;line-height:14.4px;color:var(--muted);margin-top:6px;padding:0 16px}

/* testimonials */
.testimonials{position:absolute;top:964px;left:0;width:824px;height:152px;background:var(--grey-band)}
.avatar{position:absolute;left:144px;top:58px;width:53px;height:63px;background:linear-gradient(#d9cfc3,#b9a898);border:1px solid #ddd}
.quote{position:absolute;left:221px;top:58px;width:461px;height:63px;background:var(--white);padding:8px 18px;font-family:"Noto Serif",Georgia,serif;font-style:italic;font-size:8px;line-height:15.4px;color:var(--muted)}
.quote::before{content:"";position:absolute;left:-9px;top:22px;border:9px solid transparent;border-left:0;border-right-color:var(--white)}
.quote cite{position:absolute;right:18px;bottom:8px;font-family:"Open Sans",Arial,sans-serif;font-style:normal;color:var(--green-card);font-size:8.5px}
.t-arrow{position:absolute;top:68px;font-size:24px;color:#ccc}

/* footer */
.site-footer{position:absolute;top:1116px;left:0;width:824px;height:84px;background:var(--footer);color:#ddd;text-align:center;font-size:7.8px}
.footer-links{margin-top:28px;word-spacing:2px}
.copyright{margin-top:11px}
</style>
</head>
<body>

<header class="site-header">
  <div class="brand">
    <span class="brand-dot"></span>
    <div>
      <div class="brand-name">Bright Core Flow</div>
      <div class="brand-tag">Pilates &amp; Spiral Flow Studio</div>
    </div>
  </div>
  <div class="call">Call Us: (555) 214-3090</div>
  <div class="badge" aria-hidden="true"></div>
</header>

<nav class="main-nav">
  <ul>
    <li class="active">Home</li><li>About Us</li><li>Schedule</li><li>Instructors</li><li>Rates</li><li>Contact Us</li>
  </ul>
  <div class="social" aria-label="Social links"><span></span><span></span><span></span><span></span></div>
</nav>

<section class="hero" role="img" aria-label="Photo of an instructor guiding a client through a Pilates stretch in the studio">
  <span class="hero-arrow" style="left:50px">‹</span>
  <span class="hero-arrow" style="right:50px">›</span>
  <h1 class="hero-title" style="font-weight:400">Voluptatem Explicabo Laudantium!!</h1>
</section>

<div class="card card-light">
  <h2>Schedule</h2>
  <div class="serif-sub">Upcoming Classes</div>
  <div class="pager"><span>←</span><span>→</span></div>
  <div class="row"><span class="clock"><svg width="9" height="9" viewBox="0 0 10 10"><circle cx="5" cy="5" r="4" fill="none" stroke="#333" stroke-width="1.5"/><path d="M5 2.5V5h2" stroke="#333" stroke-width="1.2" fill="none"/></svg>Group Reformer</span><span>18.30 - 20.00</span></div>
  <div class="row"><span class="clock"><svg width="9" height="9" viewBox="0 0 10 10"><circle cx="5" cy="5" r="4" fill="none" stroke="#333" stroke-width="1.5"/><path d="M5 2.5V5h2" stroke="#333" stroke-width="1.2" fill="none"/></svg>BootcampPlus</span><span>18.00 - 19.00</span></div>
  <div class="row"><span class="clock"><svg width="9" height="9" viewBox="0 0 10 10"><circle cx="5" cy="5" r="4" fill="none" stroke="#333" stroke-width="1.5"/><path d="M5 2.5V5h2" stroke="#333" stroke-width="1.2" fill="none"/></svg>PilatesMat</span><span>18.30 - 20.00</span></div>
</div>

<div class="card card-dark" style="left:298px">
  <h2>Rates</h2>
  <div class="serif-sub">25% discount for students</div>
  <div class="row"><span>Private Sessions</span><span>$75/hour</span></div>
  <div class="row"><span>Mat Classes</span><span>$120/10</span></div>
  <div class="row"><span>Group Reformer</span><span>$35/class</span></div>
</div>

<div class="card card-dark" style="left:534px">
  <h2>Personal Training</h2>
  <div class="serif-sub">Signup Today!</div>
  <div class="pt-body">
    <svg width="30" height="36" viewBox="0 0 30 36" aria-hidden="true"><rect x="1" y="1" width="24" height="32" fill="#fff"/><path d="M5 8h16M5 13h16M5 18h16M5 23h10" stroke="#4b5f2b" stroke-width="1.5"/><path d="M18 28l9-12 2 2-9 12z" fill="#fff" stroke="#4b5f2b"/></svg>
    <div>
      <p>Sed ut perspiciatis unde omnis iste natus errorvoluptatem accusantium doloremque laudantium, totam rem aperiam, eaque ipsa quae ab illo.</p>
      <span class="more">More &nbsp;➞</span>
    </div>
  </div>
</div>

<h2 class="section-title" style="top:600px">Bright Core <em>Flow</em></h2>
<p class="about-text">Bright Core Flow Pilates and Spiral Flow Studio, in the heart of Harbor Village, is a warm, inviting studio where students and teachers alike are supported and encouraged to discover and grow at an individual pace through the field of integrated movement.We offer one-on-one sessions, group reformer classes and mat classes.Our mission is to promote long-term emotional and physical health through joyful, integrated movement training and to inspire and nurture our clients to learn more deeply about themselves and connect with fellow students and the community.</p>

<h2 class="section-title" style="top:719px">What <em>We Do</em></h2>

<div class="service" style="left:61px">
  <div class="photo" role="img" aria-label="Photo of a trainer assisting a client with a resistance exercise" style="background:linear-gradient(100deg,#cfd6dc,#e0c7b2 50%,#5aa8d8)"></div>
  <h3>Elucidate vehicula existence</h3>
  <p>Lorem ipsum dolor sit amet, consectetur adipiscing elit. Ut volutpat rutrum eros sit amet sollicitudin.</p>
</div>
<div class="service" style="left:298px">
  <div class="photo" role="img" aria-label="Photo of clients working on reformer machines" style="background:linear-gradient(100deg,#b59a7a,#d8c9b5 50%,#6d6258)"></div>
  <h3>Group Reformer</h3>
  <p>Lorem ipsum dolor sit amet, consectetur adipiscing elit. Ut volutpat rutrum eros sit amet sollicitudin.</p>
</div>
<div class="service" style="left:534px">
  <div class="photo" role="img" aria-label="Photo of a group mat class in a bright studio" style="background:linear-gradient(#d8dde2,#c6ccd4 55%,#5b5c8c)"></div>
  <h3>Mat Class</h3>
  <p>Lorem ipsum dolor sit amet, consectetur adipiscing elit. Ut volutpat rutrum eros sit amet sollicitudin.</p>
</div>

<section class="testimonials">
  <h2 class="section-title" style="top:24px">Testimonials</h2>
  <span class="t-arrow" style="left:60px">‹</span>
  <span class="t-arrow" style="right:60px">›</span>
  <div class="avatar" role="img" aria-label="Portrait of the client giving the testimonial"></div>
  <blockquote class="quote">“ Nullam risus nisi, blandit a convallis nec, vehicula quis augue. Donec sed lobortis eros, at commodo magna. Fusce ullamcorper, purus ut imperdiet luctus, arcu felis accumsan nulla, ut mollis arcu lectus quis erat. Morbi enim turpis, sollicitudin vel elementum non, tempor ac velit. ”
    <cite>-Delia</cite>
  </blockquote>
</section>

<footer class="site-footer">
  <div class="footer-links">Home &nbsp;| &nbsp;About us &nbsp;| &nbsp;Schedule &nbsp;| &nbsp;Instructors &nbsp;| &nbsp;Rates &nbsp;| &nbsp;Contact</div>
  <div class="copyright">Copyright © 2015 &nbsp;Bright Core Flow. &nbsp;All rights reserved.</div>
</footer>

</body>
</html>
```